Cedar Hall letterhead

We changed our name and logo now need letterhead.
3-4/72 Harlow Street Linwood 2163
www.cedarhall.org.au
info@cedarhall.org.au
ph: 02 97584120

At this stage, we are preferencing Design #: 5398880 and Design #5401338

```html
<!DOCTYPE html>
<html lang="en">
<head>
<meta charset="utf-8">
<title>Cedar Hall Letterhead</title>
<link href="https://fonts.googleapis.com/css2?family=Arimo:wght@400&family=Work+Sans:wght@300&display=swap" rel="stylesheet">
<style>
  :root {
    --backdrop: #4a3426;
    --paper: #ffffff;
    --slate: #6f7d8a;
    --slate-text: #6b7580;
  }
  html, body {
    margin: 0;
    padding: 0;
    width: 953px;
    height: 1200px;
    overflow: hidden;
    background: var(--backdrop);
  }
  .canvas {
    position: relative;
    width: 953px;
    height: 1200px;
  }
  .letterhead {
    position: absolute;
    left: 163px;
    top: 156px;
    width: 627px;
    height: 888px;
    background: var(--paper);
    box-shadow: 0 2px 10px rgba(0,0,0,0.35);
  }
  .brand {
    position: absolute;
    left: 422px;
    top: 33px;
    display: flex;
    align-items: center;
    gap: 10px;
  }
  .brand-dot {
    width: 118px;
    height: 118px;
    border-radius: 50%;
    background: var(--slate);
    flex: none;
  }
  .brand-name {
    font-family: "Work Sans", Arial, sans-serif;
    font-weight: 300;
    font-size: 19px;
    line-height: 21px;
    letter-spacing: 0.5px;
    color: var(--slate);
    text-transform: uppercase;
    width: 64px;
  }
  .contact {
    position: absolute;
    left: 423px;
    top: 164px;
    font-family: "Arimo", Arial, sans-serif;
    font-style: normal;
    font-size: 11.5px;
    line-height: 14.3px;
    color: var(--slate-text);
  }
  .contact-address {
    margin: 0;
    text-transform: uppercase;
  }
  .contact-list {
    list-style: none;
    margin: 0;
    padding: 0;
  }
  .contact-list li {
    display: flex;
    align-items: center;
    gap: 4px;
  }
  .contact-icon {
    width: 10px;
    height: 10px;
    flex: none;
  }
</style>
</head>
<body>
<div class="canvas">
  <section class="letterhead">
    <div class="brand">
      <div class="brand-dot"></div>
      <div class="brand-name">Cedar Hall</div>
    </div>
    <address class="contact">
      <p class="contact-address">3-4/72 Harlow Street<br>Linwood 2163</p>
      <ul class="contact-list">
        <li>
          <svg class="contact-icon" viewBox="0 0 10 10" aria-hidden="true">
            <circle cx="5" cy="5" r="4.4" fill="none" stroke="var(--slate-text)" stroke-width="1"/>
            <ellipse cx="5" cy="5" rx="2" ry="4.4" fill="none" stroke="var(--slate-text)" stroke-width="0.8"/>
            <line x1="0.6" y1="5" x2="9.4" y2="5" stroke="var(--slate-text)" stroke-width="0.8"/>
          </svg>
          www.cedarhall.org.au
        </li>
        <li>
          <svg class="contact-icon" viewBox="0 0 10 10" aria-hidden="true">
            <circle cx="5" cy="5" r="5" fill="var(--slate-text)"/>
            <rect x="2.4" y="3.3" width="5.2" height="3.6" fill="#fff"/>
            <polyline points="2.4,3.3 5,5.3 7.6,3.3" fill="none" stroke="var(--slate-text)" stroke-width="0.6"/>
          </svg>
          info@cedarhall.org.au
        </li>
        <li>
          <svg class="contact-icon" viewBox="0 0 10 10" aria-hidden="true">
            <circle cx="5" cy="5" r="5" fill="var(--slate-text)"/>
            <path d="M3.2 2.6 L4.3 2.4 L4.7 3.9 L4 4.4 Q4.6 5.6 5.6 6.1 L6.1 5.4 L7.6 5.8 L7.4 6.9 Q5.2 7.4 3.6 5.2 Q2.8 3.9 3.2 2.6 Z" fill="#fff"/>
          </svg>
          02 97584120
        </li>
      </ul>
    </address>
  </section>
</div>
</body>
</html>
```